I need the Scorecard I've developed for my staff to be produced into a visually engaging piece that will encourage the staff to utilize it on a daily basis. I'm thinking it could be 5x7 in size so that it isn't too cumbersome, but I'm open to different layouts.
I have multiple other departments that will need Scorecards created for them as well, but each one will contain task specific questions for each department.

```html
<!DOCTYPE html>
<html lang="en">
<head>
<meta charset="utf-8">
<title>Receptionist Daily Excellence Scorecard</title>
<link rel="stylesheet" href="https://fonts.googleapis.com/css2?family=Open+Sans:wght@400;600;700&family=Merriweather+Sans:wght@700;800&display=swap">
<style>
:root{
  --page:#d7d8da;
  --card:#f1f1ec;
  --navy:#2b3f6e;
  --ink:#2c3340;
  --accent-text:#6f82c4;
  --yellow:#f5df2a;
  --yellow-soft:#f3f0c4;
  --panel:rgba(214,224,236,.85);
  --bar-dark:#7f91d2;
  --bar-light:#dde3f2;
  --dot-mid:#8796b6;
  --dot-light:#e6eaf3;
  --field:#ffffff;
}
*{box-sizing:border-box;margin:0;padding:0}
html,body{width:736px;height:1200px;overflow:hidden;background:var(--page)}
body{font-family:"Open Sans",Arial,sans-serif;color:var(--ink);position:relative}
.scorecard{position:absolute;left:10px;top:344px;width:716px;height:512px;background:var(--card);overflow:hidden}
.abs{position:absolute}
.divider-line{position:absolute;left:368px;top:0;height:512px;border-left:1px dashed var(--yellow)}
.title-band{position:absolute;left:0;top:16px;width:368px;height:41px;background:var(--navy);color:#fff;font-family:"Merriweather Sans",Arial,sans-serif;font-weight:800;font-size:12.4px;letter-spacing:.2px;padding:13px 0 0 26px;white-space:nowrap}
.field-label{position:absolute;top:72px;font-size:5px;font-weight:600}
.field{position:absolute;top:81px;height:18px;background:var(--field);border-radius:2px}
.field svg{position:absolute;left:5px;top:4px}
.badge{position:absolute;left:9px;top:112px;width:24px;height:24px;border-radius:50%;background:var(--yellow)}
.badge svg{position:absolute;left:6px;top:5px}
.instructions{position:absolute;left:41px;top:115px;font-size:8.2px;font-weight:700;line-height:15px;color:#3a4254;white-space:nowrap}
.panel{position:absolute;background:var(--panel);border-radius:10px}
.panel-left{left:26px;top:147px;width:271px;height:262px;--pad:12px;--cols:95px 75px 79px}
.panel-right{left:380px;top:28px;width:309px;height:291px;--pad:28px;--cols:79px 72px 81px}
.section-title{position:absolute;left:var(--pad);font-size:6.4px;font-weight:700;color:var(--ink);white-space:nowrap}
.section-rule{position:absolute;left:0;right:0;border-top:1.5px solid #fff}
.row{position:absolute;left:var(--pad);display:grid;grid-template-columns:var(--cols);align-items:center;transform:translateY(-50%)}
.task{font-size:4.3px;line-height:5.4px;padding-left:5px;position:relative;padding-right:4px}
.task::before{content:"";position:absolute;left:0;top:0;bottom:0;border-left:1px solid #9fcf7a}
.task::after{content:"";position:absolute;left:-1.5px;top:50%;width:4px;height:4px;margin-top:-2px;border-radius:50%;background:#8cc35c}
.row.head{height:8px;background:linear-gradient(90deg,transparent 95px,var(--yellow-soft) 95px)}
.row.head .task{font-size:5.4px;font-weight:700}
.row.head .task::before{display:none}
.row.head .task::after{background:var(--yellow);width:6px;height:6px;margin-top:-3px;left:-4px}
.head-label{font-size:3.4px;font-weight:700;position:relative}
.head-label.rating::after{content:"";position:absolute;left:22px;right:-6px;top:50%;border-top:1px dashed #b9b58a}
.head-label.notes{text-align:center}
.rating-dots{display:flex;gap:7px;position:relative}
.rating-dots::before{content:"";position:absolute;left:4px;right:4px;top:50%;border-top:1px dashed #9aa6c2}
.dot{position:relative;width:8px;height:8px;border-radius:50%;background:var(--navy);color:#fff;font-size:4.6px;font-weight:700;font-style:normal;display:flex;align-items:center;justify-content:center}
.dot.mid{background:var(--dot-mid)}
.dot.soft{background:var(--dot-light);color:#9aa6c2;border:.6px solid #b4bed6}
.note-bar{height:6px;border-radius:3px;background:var(--bar-light)}
.note-bar.filled{background:var(--bar-dark)}
.label-accent{position:absolute;font-size:7px;font-weight:400;color:var(--accent-text);white-space:nowrap}
.label-small{position:absolute;font-size:4px;font-weight:600;white-space:nowrap}
.box{position:absolute;background:#fff;border-radius:2px}
.summary-box{position:absolute;left:382px;top:342px;width:191px;height:40px;background:#dde4f1;border-radius:4px;padding:6px 0 0 9px;font-size:4.4px;line-height:11.6px}
.sig{position:absolute;left:528px;font-size:4.4px;display:flex;width:148px;white-space:nowrap}
.sig span{flex:1;border-bottom:.6px solid #555;margin-left:6px;margin-bottom:1px}
.manager-dots{position:absolute;left:381px;top:473px;display:flex;gap:7px}
</style>
</head>
<body>
<main class="scorecard">
  <div class="divider-line"></div>

  <header class="title-band">RECEPTIONIST DAILY EXCELLENCE SCORECARD</header>

  <span class="field-label" style="left:31px">Name</span>
  <span class="field-label" style="left:159px">Date</span>
  <span class="field-label" style="left:213px">Location</span>
  <div class="field" style="left:26px;width:118px"><svg width="8" height="9" viewBox="0 0 8 9"><circle cx="4" cy="2.5" r="2" fill="none" stroke="#444" stroke-width=".8"/><path d="M.6 8.6 C.8 5 7.2 5 7.4 8.6 Z" fill="none" stroke="#444" stroke-width=".8"/></svg></div>
  <div class="field" style="left:155px;width:44px"><svg width="9" height="9" viewBox="0 0 9 9"><rect x=".5" y="1.5" width="8" height="7" rx="1" fill="none" stroke="#444" stroke-width=".8"/><path d="M.5 3.6h8M2.5 .5v2M6.5 .5v2" stroke="#444" stroke-width=".8"/></svg></div>
  <div class="field" style="left:210px;width:143px"><svg width="7" height="9" viewBox="0 0 7 9"><path d="M3.5 8.5 C1 5.6 .5 4.4 .5 3.3 A3 3 0 0 1 6.5 3.3 C6.5 4.4 6 5.6 3.5 8.5Z" fill="none" stroke="#444" stroke-width=".8"/><circle cx="3.5" cy="3.3" r="1" fill="#444"/></svg></div>

  <div class="badge"><svg width="12" height="14" viewBox="0 0 12 14"><rect x="1" y="2" width="10" height="11" rx="1" fill="none" stroke="#2b3f6e" stroke-width="1"/><rect x="4" y="1" width="4" height="2" fill="#2b3f6e"/><path d="M3 6l1 1 2-2M3 10l1 1 2-2M7 6.5h2.5M7 10.5h2.5" stroke="#2b3f6e" stroke-width=".8" fill="none"/></svg></div>
  <p class="instructions">(Please rate yourself for each task:<br>1 = Needs Improvement, 3 = Meets Expectations, 5 = Excellent)</p>

  <section class="panel panel-left">
    <h2 class="section-title" style="top:6px">1.Call Handling &amp; First Call Intake</h2>
    <div class="row head" style="top:23px"><span class="task">Task</span><span class="head-label rating">Self-Rating</span><span class="head-label notes">Notes / Issues</span></div>
    <div class="row" style="top:35px"><span class="task">Answered 90%+ calls within 3 rings</span><span class="rating-dots"><i class="dot">1</i><i class="dot">2</i><i class="dot">3</i><i class="dot mid">4</i><i class="dot soft">5</i></span><span class="note-bar"></span></div>
    <div class="row" style="top:48px"><span class="task">Maintained empathy and professionalism</span><span class="rating-dots"><i class="dot">1</i><i class="dot">2</i><i class="dot">3</i><i class="dot mid">4</i><i class="dot soft">5</i></span><span class="note-bar"></span></div>
    <div class="row" style="top:64px"><span class="task">Accurately completed all First Call fields</span><span class="rating-dots"><i class="dot">1</i><i class="dot">2</i><i class="dot">3</i><i class="dot mid">4</i><i class="dot soft">5</i></span><span class="note-bar filled"></span></div>
    <div class="row" style="top:78px"><span class="task">Worked within Receptionist role</span><span class="rating-dots"><i class="dot">1</i><i class="dot">2</i><i class="dot">3</i><i class="dot mid">4</i><i class="dot soft">5</i></span><span class="note-bar filled"></span></div>
    <div class="section-rule" style="top:89px"></div>

    <h2 class="section-title" style="top:93px">2. Call Management During Busy Times</h2>
    <div class="row head" style="top:110px"><span class="task">Task</span><span class="head-label rating">Self-Rating</span><span class="head-label notes">Notes / Issues</span></div>
    <div class="row" style="top:122px"><span class="task">Prioritized urgent vs non-urgent calls</span><span class="rating-dots"><i class="dot">1</i><i class="dot">2</i><i class="dot">3</i><i class="dot mid">4</i><i class="dot soft">5</i></span><span class="note-bar"></span></div>
    <div class="row" style="top:135px"><span class="task">Hold times under 1 minute</span><span class="rating-dots"><i class="dot">1</i><i class="dot">2</i><i class="dot">3</i><i class="dot mid">4</i><i class="dot soft">5</i></span><span class="note-bar"></span></div>
    <div class="row" style="top:147px"><span class="task">Logged all calls</span><span class="rating-dots"><i class="dot">1</i><i class="dot">2</i><i class="dot">3</i><i class="dot mid">4</i><i class="dot soft">5</i></span><span class="note-bar filled"></span></div>
    <div class="row" style="top:165px"><span class="task">Requested help if overwhelmed</span><span class="rating-dots"><i class="dot">1</i><i class="dot">2</i><i class="dot">3</i><i class="dot mid">4</i><i class="dot soft">5</i></span><span class="note-bar filled"></span></div>
    <div class="section-rule" style="top:181px"></div>

    <h2 class="section-title" style="top:190px">3. Scheduling Accuracy</h2>
    <div class="row head" style="top:207px"><span class="task">Task</span><span class="head-label rating">Self-Rating</span><span class="head-label notes">Notes / Issues</span></div>
    <div class="row" style="top:220px"><span class="task">Updated scheduling board</span><span class="rating-dots"><i class="dot">1</i><i class="dot">2</i><i class="dot">3</i><i class="dot mid">4</i><i class="dot soft">5</i></span><span class="note-bar"></span></div>
    <div class="row" style="top:233px"><span class="task">Cross-checked with Red Book</span><span class="rating-dots"><i class="dot">1</i><i class="dot">2</i><i class="dot">3</i><i class="dot mid">4</i><i class="dot soft">5</i></span><span class="note-bar filled"></span></div>
    <div class="row" style="top:246px"><span class="task">Entered manifest info promptly</span><span class="rating-dots"><i class="dot">1</i><i class="dot">2</i><i class="dot">3</i><i class="dot mid">4</i><i class="dot soft">5</i></span><span class="note-bar filled"></span></div>
  </section>

  <h3 class="label-accent" style="left:26px;top:419px">Stars &amp; Flags (Supervisor Use Only)</h3>
  <span class="label-small" style="left:26px;top:433px">Stars (Excellence or above-and-beyond moments):</span>
  <span class="label-small" style="left:196px;top:433px">Flags (Concerns needing follow-up/coaching):</span>
  <div class="box" style="left:26px;top:443px;width:162px;height:31px"></div>
  <div class="box" style="left:196px;top:443px;width:162px;height:31px"></div>

  <section class="panel panel-right">
    <h2 class="section-title" style="top:7px">4. Clothing &amp; Flowers</h2>
    <div class="row head" style="top:26px"><span class="task">Task</span><span class="head-label rating">Self-Rating</span><span class="head-label notes">Notes / Issues</span></div>
    <div class="row" style="top:38px"><span class="task">Clothing sheet completed</span><span class="rating-dots"><i class="dot">1</i><i class="dot">2</i><i class="dot">3</i><i class="dot mid">4</i><i class="dot soft">5</i></span><span class="note-bar"></span></div>
    <div class="row" style="top:49px"><span class="task">Family contact noted on sheet</span><span class="rating-dots"><i class="dot">1</i><i class="dot">2</i><i class="dot">3</i><i class="dot mid">4</i><i class="dot soft">5</i></span><span class="note-bar"></span></div>
    <div class="row" style="top:61px"><span class="task">Floral deliveries logged</span><span class="rating-dots"><i class="dot">1</i><i class="dot">2</i><i class="dot">3</i><i class="dot mid">4</i><i class="dot soft">5</i></span><span class="note-bar filled"></span></div>
    <div class="row" style="top:73px"><span class="task">Concerns communicated to Care Center</span><span class="rating-dots"><i class="dot">1</i><i class="dot">2</i><i class="dot">3</i><i class="dot mid">4</i><i class="dot soft">5</i></span><span class="note-bar filled"></span></div>
    <div class="row" style="top:85px"><span class="task">Flower placement verified</span><span class="rating-dots"><i class="dot">1</i><i class="dot">2</i><i class="dot">3</i><i class="dot mid">4</i><i class="dot soft">5</i></span><span class="note-bar filled"></span></div>
    <div class="section-rule" style="top:98px"></div>

    <h2 class="section-title" style="top:107px">5. Death Certificates</h2>
    <div class="row head" style="top:124px"><span class="task">Task</span><span class="head-label rating">Self-Rating</span><span class="head-label notes">Notes / Issues</span></div>
    <div class="row" style="top:136px"><span class="task">Verified recipient ID &amp; relationship</span><span class="rating-dots"><i class="dot">1</i><i class="dot">2</i><i class="dot">3</i><i class="dot mid">4</i><i class="dot soft">5</i></span><span class="note-bar"></span></div>
    <div class="row" style="top:150px"><span class="task">Confirmed correct documents enclosed</span><span class="rating-dots"><i class="dot">1</i><i class="dot">2</i><i class="dot">3</i><i class="dot mid">4</i><i class="dot soft">5</i></span><span class="note-bar"></span></div>
    <div class="row" style="top:164px"><span class="task">Recipient signed the DC logbook</span><span class="rating-dots"><i class="dot">1</i><i class="dot">2</i><i class="dot">3</i><i class="dot mid">4</i><i class="dot soft">5</i></span><span class="note-bar filled"></span></div>
    <div class="row" style="top:179px"><span class="task">Suggested proofreading before leaving</span><span class="rating-dots"><i class="dot">1</i><i class="dot">2</i><i class="dot">3</i><i class="dot mid">4</i><i class="dot soft">5</i></span><span class="note-bar filled"></span></div>
    <div class="section-rule" style="top:196px"></div>

    <h2 class="section-title" style="top:207px">6. Routing &amp; Messages</h2>
    <div class="row head" style="top:223px"><span class="task">Task</span><span class="head-label rating">Self-Rating</span><span class="head-label notes">Notes / Issues</span></div>
    <div class="row" style="top:236px"><span class="task">Calls routed appropriately</span><span class="rating-dots"><i class="dot">1</i><i class="dot">2</i><i class="dot">3</i><i class="dot mid">4</i><i class="dot soft">5</i></span><span class="note-bar"></span></div>
    <div class="row" style="top:250px"><span class="task">Messages included all required info</span><span class="rating-dots"><i class="dot">1</i><i class="dot">2</i><i class="dot">3</i><i class="dot mid">4</i><i class="dot soft">5</i></span><span class="note-bar"></span></div>
    <div class="row" style="top:268px"><span class="task">Delivered 99%+ messages in 30 min</span><span class="rating-dots"><i class="dot">1</i><i class="dot">2</i><i class="dot">3</i><i class="dot mid">4</i><i class="dot soft">5</i></span><span class="note-bar filled"></span></div>
  </section>

  <h3 class="label-accent" style="left:382px;top:328px">Daily Status Summary (Circle One)</h3>
  <div class="summary-box">
    Excellent – All key duties completed, proactive, calm under pressure<br>
    Satisfactory – Most duties completed, minor follow-up needed<br>
    Needs Support – Missed urgent duties, accuracy or stress issues
  </div>

  <svg class="abs" style="left:588px;top:322px" width="62" height="64" viewBox="0 0 62 64" aria-label="Rising bar chart icon">
    <rect x="2" y="46" width="9" height="17" rx="1.5" fill="#3b4657"/>
    <rect x="15" y="36" width="9" height="27" rx="1.5" fill="#3b4657"/>
    <rect x="28" y="26" width="9" height="37" rx="1.5" fill="#3b4657"/>
    <rect x="41" y="15" width="9" height="48" rx="1.5" fill="#3b4657"/>
    <path d="M0 34 C18 30 34 18 50 5" stroke="#2f7fc8" stroke-width="3.2" fill="none"/>
    <path d="M42 3 L56 0 L52 13 Z" fill="#2f7fc8"/>
  </svg>

  <h3 class="label-accent" style="left:382px;top:394px">Daily Reflection</h3>
  <span class="label-small" style="left:382px;top:407px">What went well today?</span>
  <span class="label-small" style="left:485px;top:407px">Any issues or barriers to note?</span>
  <span class="label-small" style="left:586px;top:407px">Support needed from supervisor?</span>
  <div class="box" style="left:382px;top:415px;width:97px;height:25px"></div>
  <div class="box" style="left:485px;top:415px;width:96px;height:25px"></div>
  <div class="box" style="left:586px;top:415px;width:97px;height:25px"></div>

  <h3 class="label-accent" style="left:382px;top:446px">Manager's Overall Rating</h3>
  <span class="label-small" style="left:382px;top:456px">(Manager: Please rate overall performance on a 1-5 scale)</span>
  <span class="label-small" style="left:382px;top:464px;color:var(--accent-text)">Manager Overall Rating (1-5)</span>
  <div class="manager-dots rating-dots"><i class="dot">1</i><i class="dot">2</i><i class="dot">3</i><i class="dot mid">4</i><i class="dot soft">5</i></div>

  <div class="sig" style="top:450px">Receptionist Signature:<span></span></div>
  <div class="sig" style="top:462px">Supervisor Signature:<span></span></div>
  <div class="sig" style="top:478px">Date:<span></span></div>
</main>
</body>
</html>
```